Agricultural Consulting Website

Provide a modern yet business like website for my new Agriculture Consulting Business in Australia called FieldNorth. Whilst we are based in Australia we are targetting both domestic and international markets (especially in Asia). We are targetting corporate, small business, government and farmer clients. The design should compliment our logo also sourced through pixel harbor. The webiste should be easy for me to keep updated on a regular basis without the need to go back to the designer.

Industry/Entity Type

Business

Requirements
Must have
• clean crisp feel
• be modern yet business like
• be able to be updated by myself easily

```html
<!DOCTYPE html>
<html lang="en">
<head>
<meta charset="utf-8">
<title>FieldNorth Agriculture Consulting</title>
<link rel="stylesheet" href="https://fonts.googleapis.com/css2?family=Open+Sans:ital,wght@0,400;0,600;0,700;1,400;1,600;1,700&display=swap">
<style>
  :root {
    --page: #ffffff;
    --cream: #fde8a8;
    --green: #007a00;
    --brown: #6b3a0c;
    --ink: #111111;
    --card: #ffffff;
    --leaf: #3a8a1c;
  }
  * { box-sizing: border-box; margin: 0; padding: 0; }
  html, body { width: 1200px; height: 900px; overflow: hidden; }
  body {
    background: var(--page);
    font-family: "Open Sans", Arial, sans-serif;
    color: var(--ink);
    position: relative;
  }
  .site {
    position: absolute; left: 60px; top: 0;
    width: 1082px; height: 900px;
    background: var(--cream);
  }
  .abs { position: absolute; }

  .brand { left: 143px; top: 19px; display: flex; align-items: center; gap: 8px; }
  .brand-mark { width: 65px; height: 67px; background: var(--brown); }
  .brand-name { font-size: 28px; font-weight: 600; color: var(--leaf); letter-spacing: -0.5px; white-space: nowrap; }
  .tagline { left: 381px; top: 44px; font-size: 12.5px; font-weight: 700; white-space: nowrap; letter-spacing: -0.1px; }
  .social { left: 791px; top: 38px; display: flex; gap: 14px; }
  .social span {
    width: 27px; height: 27px; border-radius: 50%;
    background: var(--leaf);
    box-shadow: 0 2px 2px rgba(0,0,0,.45);
  }

  .nav { left: 0; top: 104px; width: 1082px; height: 53px; background: var(--green); }
  .nav ul { list-style: none; position: absolute; left: 160px; top: 17px; display: flex; }
  .nav li { font-size: 11.5px; color: #111; margin-right: 31px; line-height: 20px; white-space: nowrap; }
  .nav li.contact { background: #fff; padding: 0 4px; margin-right: 0; margin-left: -1px; }

  .headline { left: 0; width: 1082px; top: 172px; text-align: center; }
  .headline h1 {
    display: inline-block; font-size: 33px; font-weight: 700; font-style: italic;
    color: var(--green); border-bottom: 2px solid var(--green); line-height: 40px;
  }
  .headline p { font-size: 18.5px; font-weight: 700; font-style: italic; color: var(--green); margin-top: 6px; white-space: nowrap; }

  .card { background: var(--card); box-shadow: 0 1px 4px rgba(0,0,0,.45); }
  .card-feature { left: 143px; top: 264px; width: 502px; height: 294px; }
  .photo-feature {
    left: 14px; top: 13px; width: 474px; height: 263px;
    background: linear-gradient(135deg, #b8331c 0%, #6a8f2a 40%, #e8e6e0 55%, #4f8a22 75%, #c9421f 100%);
  }
  .card-gallery { left: 658px; top: 264px; width: 267px; height: 556px; }
  .photo { left: 24px; width: 219px; height: 145px; }
  .photo-lettuce { top: 26px; background: linear-gradient(160deg, #8fd33a, #3f9a16); }
  .photo-berries { top: 206px; background: linear-gradient(160deg, #f05a7a, #c81c48); }
  .photo-blue { top: 383px; background: linear-gradient(160deg, #4c63b8, #1b2a6a); }

  .intro { left: 151px; top: 580px; width: 490px; }
  .intro h2 { font-size: 21px; font-weight: 400; white-space: nowrap; }
  .intro p { width: 478px; font-size: 10.8px; line-height: 19.3px; margin: 16px 0 0 4px; letter-spacing: -0.15px; }
  .intro h3 { font-size: 14px; font-weight: 400; margin: 18px 0 0 4px; }
  .intro h4 { font-size: 14px; font-weight: 400; font-style: italic; margin: 8px 0 0 4px; }
  .intro p.area { width: 460px; margin-top: 4px; text-indent: 6px; }

  .footer { left: 0; top: 843px; width: 1082px; height: 57px; background: var(--green); }
  .footer small { position: absolute; left: 158px; top: 24px; font-size: 12px; white-space: nowrap; }
  .footer ul { position: absolute; left: 537px; top: 22px; list-style: none; display: flex; font-size: 11px; font-weight: 600; white-space: nowrap; }
  .footer li + li::before { content: "|"; margin: 0 7px; }
</style>
</head>
<body>
<div class="site">
  <header>
    <div class="abs brand">
      <span class="brand-mark"></span>
      <span class="brand-name">FieldNorth</span>
    </div>
    <div class="abs tagline">FieldNorth Agriculture Consulting &nbsp;-&nbsp; in a fully sustainable way</div>
    <div class="abs social" aria-label="Social links">
      <span></span><span></span><span></span><span></span>
    </div>
  </header>

  <nav class="abs nav">
    <ul>
      <li>HOME</li><li>ABOUT</li><li>PRODUCT</li><li>SERVICES</li><li>CLIENTS</li>
      <li>MEDIA</li><li>GALLERY</li><li>RESOURCES</li><li>CAREERS</li>
      <li class="contact">CONTACT US</li>
    </ul>
  </nav>

  <section class="abs headline">
    <h1>60% or 590 million hectares</h1>
    <p>FieldNorth Agriculture share of the worlds total amount of uncultivated, arable land</p>
  </section>

  <div class="abs card card-feature">
    <div class="abs photo-feature" role="img" aria-label="Fresh vegetables around a shopping list notepad"></div>
  </div>

  <aside class="abs card card-gallery">
    <div class="abs photo photo-lettuce" role="img" aria-label="Green lettuce leaves"></div>
    <div class="abs photo photo-berries" role="img" aria-label="Fresh raspberries"></div>
    <div class="abs photo photo-blue" role="img" aria-label="Fresh blueberries"></div>
  </aside>

  <main class="abs intro">
    <h2>Welcome to FieldNorth Agriculture Consulting</h2>
    <p>Lorem ipsum dolor sit amet, consectetur adipiscing elit. Sed at ante. Mauris eleifend, quam a vulputate dictum, massa quam dapibus leo, eget vulputate orci purus ut lorem. In fringilla mi in ligula. Pellentesque aliquam quam vel dolor. Nunc adipiscing. Sed quam odio, tempus ac, aliquam molestie, varius ac, tellus. Vestibulum ut nulla aliquam risus rutrum interdum.</p>
    <h3>Key Areas of Operation</h3>
    <h4>Advisory</h4>
    <p class="area">Lorem ipsum dolor sit amet, consectetur adipiscing elit. Sed at ante. Mauris eleifend, quam a vulputate dictum, massa quam dapibus leo, eget vulputate orci purus ut lorem.</p>
  </main>

  <footer class="abs footer">
    <small>@ 2013 FieldNorth All Rights Reserved</small>
    <ul>
      <li>Home</li><li>About</li><li>Product</li><li>Services</li><li>Clients</li><li>Gallery</li><li>Contact Us</li>
    </ul>
  </footer>
</div>
</body>
</html>
```